Analytics software company needs a business card design

We need a business card design for a global analytics software provider called 'Varnel Software'. Our main focus is developing real estate analysis software. We are open to any color scheme. The final design should be simple, modern, and precise.
Updates

There is one day left in our project and we are still looking forward to receiving additional submissions. We look forward to selecting one of your designs. Thanks.

Industry/Entity Type

Real Estate

```html
<!DOCTYPE html>
<html lang="en">
<head>
<meta charset="utf-8">
<title>Varnel Software — Business Card</title>
<link rel="stylesheet" href="https://fonts.googleapis.com/css2?family=Titillium+Web:wght@400;600;700&display=swap">
<style>
  :root {
    --page: #e9e7e4;
    --card-white: #ffffff;
    --card-dark: #25272c;
    --accent: #f26a21;
    --brand-navy: #2a3b7c;
    --muted: #6d6f74;
    --light-text: #f1f1f1;
  }
  * { box-sizing: border-box; margin: 0; padding: 0; }
  html, body { width: 1200px; height: 1000px; overflow: hidden; }
  body {
    background: var(--page);
    font-family: "Titillium Web", Arial, sans-serif;
    position: relative;
  }
  .card {
    position: absolute;
    left: 250px;
    width: 700px;
    height: 400px;
    overflow: hidden;
    box-shadow: 0 6px 18px rgba(0,0,0,0.18);
  }
  /* Front */
  .card-front { top: 60px; background: var(--card-dark); }
  .front-top {
    position: absolute; left: 0; top: 0; width: 100%; height: 160px;
    background: var(--card-white);
    border-bottom: 4px solid var(--accent);
  }
  .brand { position: absolute; left: 60px; top: 48px; display: flex; align-items: center; gap: 14px; }
  .brand-dot { width: 46px; height: 46px; border-radius: 50%; background: var(--accent); flex: none; }
  .brand-name { font-weight: 700; font-size: 40px; line-height: 1; color: var(--brand-navy); }
  .brand-tagline { position: absolute; left: 120px; top: 94px; font-size: 17px; color: var(--muted); }
  .person { position: absolute; left: 60px; top: 268px; }
  .person-name { font-size: 38px; font-weight: 600; color: var(--accent); line-height: 1; }
  .person-role { font-size: 18px; color: var(--light-text); margin-top: 6px; }
  .contacts { position: absolute; left: 400px; top: 196px; color: var(--light-text); font-size: 16px; line-height: 1.35; }
  .address { margin-bottom: 6px; }
  .contact-row { display: flex; align-items: center; gap: 10px; height: 26px; }
  .contact-row svg { width: 16px; height: 16px; flex: none; }
  /* Back */
  .card-back { top: 540px; background: var(--card-dark); }
  .back-band {
    position: absolute; left: 0; top: 120px; width: 100%; height: 160px;
    background: var(--accent);
  }
  .back-brand { position: absolute; left: 0; right: 0; top: 40px; display: flex; justify-content: center; align-items: center; gap: 14px; }
  .back-brand .brand-dot { background: var(--card-white); }
  .back-brand .brand-name { color: var(--card-white); }
  .back-tagline { position: absolute; left: 0; right: 0; top: 96px; text-align: center; font-size: 17px; color: var(--card-white); }
</style>
</head>
<body>
  <section class="card card-front" aria-label="Business card front">
    <div class="front-top">
      <div class="brand">
        <span class="brand-dot"></span>
        <span class="brand-name">Varnel Software</span>
      </div>
      <p class="brand-tagline">developing real estate analysis software</p>
    </div>
    <div class="person">
      <p class="person-name">Daniel Hale</p>
      <p class="person-role">President Director</p>
    </div>
    <div class="contacts">
      <p class="address">4200 Linden Ct,<br>Riverdale, MD 20737, USA</p>
      <div class="contact-row">
        <svg viewBox="0 0 16 16" aria-hidden="true"><path d="M3 1h3l1 4-2 1c1 2 3 4 5 5l1-2 4 1v3c0 1-1 2-2 2C7 15 1 9 1 3c0-1 1-2 2-2z" fill="#f26a21"/></svg>
        <span>+1 555 010 246</span>
      </div>
      <div class="contact-row">
        <svg viewBox="0 0 16 16" aria-hidden="true"><rect x="1" y="3" width="14" height="10" fill="#f26a21"/><path d="M1 3l7 6 7-6" fill="none" stroke="#25272c" stroke-width="1.5"/></svg>
        <span>info@varnel-software.com</span>
      </div>
      <div class="contact-row">
        <svg viewBox="0 0 16 16" aria-hidden="true"><circle cx="8" cy="8" r="6.5" fill="none" stroke="#f26a21" stroke-width="2"/><path d="M1.5 8h13M8 1.5c-3 3-3 10 0 13M8 1.5c3 3 3 10 0 13" fill="none" stroke="#f26a21" stroke-width="1.3"/></svg>
        <span>www.varnel-software.com</span>
      </div>
    </div>
  </section>

  <section class="card card-back" aria-label="Business card back">
    <div class="back-band">
      <div class="back-brand">
        <span class="brand-dot"></span>
        <span class="brand-name">Varnel Software</span>
      </div>
      <p class="back-tagline">developing real estate analysis software</p>
    </div>
  </section>
</body>
</html>
```